Harborlight Venture Studio (HVS)

Create a Flyer similar to the example or better

Target Market(s)

Management of Corporate Companies

Requirements
Must have
• follow the PDF-example
Nice to have
• compelling

```html
<!DOCTYPE html>
<html lang="en">
<head>
<meta charset="utf-8">
<title>Harborlight Venture Studio – Innovation Flyer</title>
<link rel="stylesheet" href="https://fonts.googleapis.com/css2?family=Lato:wght@400;700;900&display=swap">
<style>
  :root{
    --navy:#1c1f4f;
    --navy-deep:#15173f;
    --gold:#c9a84a;
    --gold-light:#e0c77a;
    --sky-top:#3f86c7;
    --sky-low:#a9d0ea;
    --sea:#1f7f86;
    --foam:#eef4f6;
    --ink:#222436;
    --paper:#ffffff;
    --mist:#e9ebee;
  }
  *{margin:0;padding:0;box-sizing:border-box}
  html,body{width:1200px;height:848px;overflow:hidden;background:var(--paper)}
  .flyer{position:relative;width:1200px;height:848px;overflow:hidden;font-family:'Lato',Arial,sans-serif;color:var(--ink);background:var(--paper)}
  .artwork{position:absolute;inset:0}
  .panel{position:absolute}
  .panel h2{font-weight:900;font-size:14.2px;line-height:17px;color:var(--navy);text-align:center;text-transform:uppercase;letter-spacing:.1px}
  .panel p{font-size:10.1px;line-height:12.9px;letter-spacing:-.08px;text-align:justify;margin-bottom:9px}
  .panel p.indent{text-indent:6px}
  .panel--left{left:46px;top:402px;width:318px}
  .panel--left h2{margin-bottom:24px}
  .panel--middle{left:433px;top:402px;width:333px}
  .panel--middle h2{margin-bottom:24px}
  .panel--right{left:836px;top:307px;width:336px}
  .panel--right h2{margin-bottom:7px}
  .copyright{position:absolute;left:433px;top:795px;width:333px;text-align:center;font-weight:700;font-size:10.6px;color:var(--navy)}
  .brand-mark{position:absolute;left:930px;top:120px;display:flex;align-items:center;gap:12px}
  .brand-mark__dot{width:26px;height:26px;border-radius:50%;background:var(--gold)}
  .brand-mark__name{font-weight:900;font-size:21px;line-height:24px;color:var(--paper)}
  .contact{position:absolute;left:800px;top:744px;width:400px;color:var(--paper)}
  .contact__name{text-align:center;font-weight:900;font-size:14px;letter-spacing:.2px}
  .contact__address{display:flex;align-items:center;gap:9px;margin:9px 0 0 72px;font-size:11.5px}
  .contact__lines{display:flex;align-items:center;margin:12px 0 0 66px;font-size:11px;line-height:14px}
  .contact__group{display:flex;align-items:center;gap:8px}
  .contact__divider{width:1px;height:28px;background:var(--paper);margin:0 14px}
  .contact svg{flex:none}
</style>
</head>
<body>
<div class="flyer">

  <svg class="artwork" width="1200" height="848" viewBox="0 0 1200 848">
    <defs>
      <linearGradient id="skySea" x1="0" y1="0" x2="0" y2="1">
        <stop offset="0" stop-color="#2f78bd"/>
        <stop offset=".45" stop-color="var(--sky-low)"/>
        <stop offset=".62" stop-color="#cfe3ee"/>
        <stop offset=".8" stop-color="#2f8f96"/>
        <stop offset="1" stop-color="#1a5f86"/>
      </linearGradient>
      <linearGradient id="mistLeft" x1="0" y1="0" x2="1" y2="1">
        <stop offset="0" stop-color="#cfd3d8"/>
        <stop offset=".55" stop-color="#eef0f2"/>
        <stop offset="1" stop-color="#dfe2e6"/>
      </linearGradient>
      <linearGradient id="mistRight" x1="0" y1="0" x2="0" y2="1">
        <stop offset="0" stop-color="#f1f2f4"/>
        <stop offset="1" stop-color="#d9dce0"/>
      </linearGradient>
    </defs>

    <rect class="mist-left" x="0" y="300" width="400" height="548" fill="url(#mistLeft)" role="img" aria-label="Faded grey photograph of a breaking ocean wave"/>
    <rect class="mist-right" x="800" y="250" width="400" height="500" fill="url(#mistRight)" role="img" aria-label="Faded grey photograph of ocean spray"/>
    <rect class="panel-sheet" x="400" y="330" width="400" height="518" fill="var(--paper)"/>

    <path class="hero-photo" role="img" aria-label="Photograph of a surfer riding a large curling turquoise wave under a blue sky"
      d="M0 0 H1200 V226 C1080 214 960 236 820 270 C680 304 540 328 400 330 C250 332 120 305 0 268 Z" fill="url(#skySea)"/>

    <path class="swoosh-gold" d="M0 268 C120 305 250 332 400 330 C540 328 680 304 820 270 C960 236 1080 214 1200 226 V250 C1080 246 960 262 820 292 C660 326 520 350 400 352 C240 354 110 328 0 300 Z" fill="var(--gold)"/>
    <path class="swoosh-navy" d="M210 330 C300 345 360 350 420 350 C560 348 700 318 840 282 C960 252 1060 236 1140 232 C1060 246 960 266 840 300 C700 340 560 372 430 376 C360 378 290 362 210 330 Z" fill="var(--navy)"/>

    <path class="footer-left-gold" d="M0 790 C140 806 280 830 400 844 V848 H0 Z" fill="var(--gold)"/>
    <path class="footer-left-navy" d="M0 798 C140 814 270 836 370 848 H0 Z" fill="var(--navy)"/>

    <path class="footer-right-gold" d="M800 770 C900 742 1040 722 1200 716 V730 C1040 736 900 756 800 786 Z" fill="var(--gold)"/>
    <path class="footer-right-navy" d="M800 782 C900 752 1040 732 1200 726 V848 H800 Z" fill="var(--navy)"/>
  </svg>

  <div class="brand-mark">
    <span class="brand-mark__dot"></span>
    <span class="brand-mark__name">Harborlight<br>Venture Studio</span>
  </div>

  <section class="panel panel--left">
    <h2>Innovation on demand and where it originates...</h2>
    <p>The most valid and promising source of sustained innovation of your specific business will be found within your organization's collective genius and creativity. Your organization has all necessary resources for the innovation of your business at hand. The problem is: These valuable resources are either engaged in the fulfilling of your corporate traditional business requirements or they are currently struggling with the integration of an “innovative” acquisition your corporate company has to handle.</p>
    <p class="indent">How might you access and leverage the inherent genius of your organization to develop new products and services for the era of “Disruptive Innovation”? The scale of Innovation your corporate business really demands will most recently not have taken place with the standard environment of the day-to-day business attitude. Innovation needs change, inspiration, and a conceptional thinking out of the box.</p>
    <p class="indent">Considering this, we have created a structured but nevertheless fully scalable and adjustable modular innovation process – Innovation results based on the principals of the “Theory U” by R. Ottmar Lindqvist, Design Thinking (Brightfield Studio), Neurolinguistic Programming (NLP) and some other Agile and other SCRUM methodologies more. The complete process will be executed by the experts in your organization during (max.) 5 days, in our pre-configured agile innovation facility located and ready to use on a country estate in Italy.</p>
  </section>

  <section class="panel panel--middle">
    <h2>Disruptive innovation and what it means for your corporate business...</h2>
    <p>As a striking example, let us briefly look at the fact and the consequence of “Disruptive Innovation” in the area of “Diabetes Care Products”. Imagine – you are the owner of a production site of let's say “Diabetes Products” for which you have to implement a huge number of regulations and processes – all the while, additionally having to facilitate a remarkable value of assets, to produce products you will need for the fulfilling of your customer's needs.</p>
    <p class="indent">The corporate thinking of your organization runs on the fact of keeping your business alive, vital, and productive. You will most recently have not become aware of the fact that one huge organization, being totally out of the scope of your competitor analyses, is currently inventing a device which makes 90 percent of your products and services obsolete. And if this fact is not astonishing enough, here is one more remarkable fact: A tiny little organization and newly established business in the US, is currently developing and certifying a substituting remedy for the Diabetes disease you have been creating your revenue with, over decades.</p>
    <p>And here comes the burning question to the innovation capacity of your corporate organization: How come all your experts and all your organization's expertise was not able to foresee nor to anticipate this fact of “Disruptive Innovation” of approximately 90 percent of your corporate business? How come the rights and patents are not one of your organization's assets?</p>
  </section>
  <div class="copyright">Copyright Harborlight Venture Studio LLC</div>

  <section class="panel panel--right">
    <h2>The current situation all “corporate businesses” are currently facing...</h2>
    <p>How your corporate business will be enabled to succeed in the era of “Disruptive Innovation”?</p>
    <p>Here is the fact: Your corporate business is designed to stay in compliance with demanding regulations and it has to obey to rules of the processes. GxP, FDA and GRC and numberless additional business specific regulations and requirements are representing a framework of major influencers enabling and supporting the success of your established business and go-to-market models.</p>
    <p class="indent">We totally agree: Compliance and regulations are key to operating a successful corporate business organization. However, on the other hand, there are these regulations slowing down, hindering or even disabling your capacity to innovate within the era of “Disruptive Innovation”. If we talk about “Disruptive Innovation”, we mean exactly that: Disruption - of traditional collaboration attitudes and unchanged continuation of corporate business organizations. In our era, corporate organizations of all kinds need more than just elaborating around the symptoms and trying to handle them by simple implementation attempts of new IT-Infrastructures – corporate businesses need desperately a true and honest reflection upon the existing facts and in the consequence, they have to come up with valid answers to the profound challenges of the drastically changing business challenges ahead.</p>
    <p class="indent">How can you expect your corporate organization to innovate on products, processes or global synergetic collaboration, if your people and your organization are 100 percent engaged in fulfilling and ensuring the functioning of given requirements in the context of your corporate business?</p>
  </section>

  <footer class="contact">
    <div class="contact__name">Harborlight Venture Studio LLC</div>
    <div class="contact__address">
      <svg width="12" height="16" viewBox="0 0 12 16" aria-hidden="true"><path d="M6 0C2.7 0 0 2.6 0 5.9 0 10.2 6 16 6 16s6-5.8 6-10.1C12 2.6 9.3 0 6 0zm0 8.3A2.4 2.4 0 1 1 6 3.5a2.4 2.4 0 0 1 0 4.8z" fill="var(--gold)"/></svg>
      <span>Seeblickweg 7 CH – 6400 Altmatt / LU</span>
    </div>
    <div class="contact__lines">
      <div class="contact__group">
        <svg width="18" height="22" viewBox="0 0 18 22" aria-hidden="true"><path d="M4 1l3 5-2 2c1 3 3 5 6 7l2-2 4 3-2 4C8 19 1 12 1 4z" fill="none" stroke="var(--gold)" stroke-width="1.8" stroke-linejoin="round"/></svg>
        <span>+41 41 555 01 20<br>+41 79 555 0147</span>
      </div>
      <span class="contact__divider"></span>
      <div class="contact__group">
        <svg width="14" height="32" viewBox="0 0 14 32" aria-hidden="true"><circle cx="7" cy="7" r="6" fill="var(--gold)"/><text x="7" y="10" font-size="9" text-anchor="middle" fill="var(--navy)" font-family="Lato, sans-serif" font-weight="900">@</text><circle cx="7" cy="24" r="6" fill="none" stroke="var(--gold)" stroke-width="1.4"/><path d="M1 24h12M7 18c-3 4-3 8 0 12M7 18c3 4 3 8 0 12" fill="none" stroke="var(--gold)" stroke-width="1"/></svg>
        <span>office@harborlight-vs.com<br>www.harborlight-vs.com</span>
      </div>
    </div>
  </footer>

</div>
</body>
</html>
```